Labels for essential oils small botlles

We are Slovenia based company Velnira Botanic Ltd. www.velnira-botanic.com We offer essential oils as pure essential oils or blends (mixed) essential oils. We have different kind of essential oils 40+ and blends. We sell in different sizes as: 10ml, 30ml, 50ml and 100ml. But majority is 10ml.
All essential oils are in glass bottles with closer. We will now change bottles style from amber to cobalt blue with black closure (see picture attached)
We would like to have different stile of label for different category of essential oils. Here is link about different categories of essential oils https://www.vialquarry.com/mixing-guides/ . The different style / color could be by note:
- Top notes
- Middle notes
- Base notes
- Mixes – different oils mixed together and named as chill out, deep breath, sleep well, etc
Possible is also differentiation regarding:
• Citrus
• Floral
• Herbaceous
• Camphoraceous
• Spicy
• Resinous
• Woody
• Earthy
• Mixes

On labels should be also pictograms according to REACH directive of EU and label according to CPL (see attached file). We would also like to add EAN code attached on the edge of the label. On label is some text fixed I try to show in pdf attached file and some is variable depends from essential oil and date of production.

Meaning we need general labels for each note or other classification and one for mixes – you could also show your option or classification on something else with story behind.

10 ml roll 30 mm x 70 mm (1,25”x3”) but finial dimensions will follow.

We use Tessaro Qm700 printer. For editing labels we use BarTender which support also EAN codes. We import labels as picture in background or different according to your instructions.

Target Market(s)

Retail, health and wellness, all audiences and web shop

Industry/Entity Type

Health And Wellness

Font styles to use
Other font styles liked:
• GillLigHr is our font but could be different

Colors

Designer to choose colors to be used in the design.

Requirements
Must have
• Label should be as template that we could use for different oils in same group. More in attached document. According to CLP we have to put red pictograms on labels which is not nice and should be some how nicely integrated. on the edge EAB dar code that products could be sell through online.
Nice to have
• Different colours, some symbol as a drop or flower or herb. Logo is not necessary that is on label. We would like that label it self represent our brand.

```html
<!DOCTYPE html>
<html lang="en">
<head>
<meta charset="utf-8">
<title>Velnira Botanic – Essential Oil Labels</title>
<link rel="stylesheet" href="https://fonts.googleapis.com/css2?family=Cormorant+Garamond:wght@500&family=Barlow+Condensed:wght@400;500;600&display=swap">
<style>
  :root {
    --bg: #f2f2f2;
    --ink: #1a1a1a;
    --label-black: #0c0c0c;
    --label-white: #f4f4f4;
    --band-text: #2a2a2a;
    --tea-tree: #62c6d2;
    --lilac: #aaa6dc;
    --grapefruit: #9fb1e2;
    --bergamot: #93cfa0;
    --peppermint: #6fc57d;
    --marjoram: #a9d96f;
  }
  * { margin: 0; padding: 0; box-sizing: border-box; }
  html, body { width: 1200px; height: 1200px; overflow: hidden; background: var(--bg); }
  .canvas { position: relative; width: 1200px; height: 1200px; background: var(--bg); }

  .brand-name {
    position: absolute; top: 222px; left: 0; width: 100%;
    text-align: center;
    font-family: "Cormorant Garamond", serif;
    font-weight: 500; font-size: 38px; letter-spacing: 2px;
    color: var(--ink);
  }

  .label-row {
    position: absolute; top: 802px; left: 135px;
    display: flex; gap: 6px;
  }
  .label {
    --accent: var(--tea-tree);
    width: 150px; height: 198px;
    background: var(--label-black);
    display: flex; flex-direction: column;
    font-family: "Barlow Condensed", sans-serif;
  }
  .label-band {
    height: 22px; background: var(--accent);
    display: flex; align-items: center; justify-content: center;
    font-family: "Cormorant Garamond", serif;
    font-size: 10px; letter-spacing: 0.6px; color: var(--band-text);
  }
  .label-body { padding: 14px 16px 0 17px; flex: 1; display: flex; flex-direction: column; }
  .label-claim { font-size: 8.5px; font-weight: 500; color: var(--label-white); letter-spacing: 0.2px; }
  .label-title {
    font-size: 25px; font-weight: 500; color: var(--label-white);
    line-height: 1; margin-top: 3px; letter-spacing: 0.3px;
    padding-bottom: 4px; border-bottom: 1px solid var(--label-white);
  }
  .oil-name { font-size: 15px; font-weight: 500; color: var(--accent); margin-top: 6px; line-height: 1.1; }
  .oil-latin { font-size: 10.5px; color: var(--accent); line-height: 1.2; }
  .label-volume { margin-top: auto; margin-bottom: 26px; font-size: 10px; font-weight: 600; color: var(--label-white); }

  .label--lilac { --accent: var(--lilac); }
  .label--grapefruit { --accent: var(--grapefruit); }
  .label--bergamot { --accent: var(--bergamot); }
  .label--peppermint { --accent: var(--peppermint); }
  .label--marjoram { --accent: var(--marjoram); }
</style>
</head>
<body>
<main class="canvas">
  <div class="brand-name">VELNIRA BOTANIC</div>

  <section class="label-row">
    <article class="label">
      <div class="label-band">VELNIRA BOTANIC</div>
      <div class="label-body">
        <p class="label-claim">100% PURE &amp; NATURAL</p>
        <h2 class="label-title">ESSENTIAL OIL</h2>
        <p class="oil-name">Tea Tree</p>
        <p class="oil-latin">Melaleuca alternifolia</p>
        <p class="label-volume">10ML I 0.3 OZ</p>
      </div>
    </article>
    <article class="label label--lilac">
      <div class="label-band">VELNIRA BOTANIC</div>
      <div class="label-body">
        <p class="label-claim">100% PURE &amp; NATURAL</p>
        <h2 class="label-title">ESSENTIAL OIL</h2>
        <p class="oil-name">Lilac</p>
        <p class="oil-latin">Lavendula officinalis</p>
        <p class="label-volume">10ML I 0.3 OZ</p>
      </div>
    </article>
    <article class="label label--grapefruit">
      <div class="label-band">VELNIRA BOTANIC</div>
      <div class="label-body">
        <p class="label-claim">100% PURE &amp; NATURAL</p>
        <h2 class="label-title">ESSENTIAL OIL</h2>
        <p class="oil-name">Grapefruit</p>
        <p class="oil-latin">Citrus paradisi</p>
        <p class="label-volume">10ML I 0.3 OZ</p>
      </div>
    </article>
    <article class="label label--bergamot">
      <div class="label-band">VELNIRA BOTANIC</div>
      <div class="label-body">
        <p class="label-claim">100% PURE &amp; NATURAL</p>
        <h2 class="label-title">ESSENTIAL OIL</h2>
        <p class="oil-name">Bergamotka</p>
        <p class="oil-latin">Citrus bergamia</p>
        <p class="label-volume">10ML I 0.3 OZ</p>
      </div>
    </article>
    <article class="label label--peppermint">
      <div class="label-band">VELNIRA BOTANIC</div>
      <div class="label-body">
        <p class="label-claim">100% PURE &amp; NATURAL</p>
        <h2 class="label-title">ESSENTIAL OIL</h2>
        <p class="oil-name">Pepper meta</p>
        <p class="oil-latin">Mentha piperita</p>
        <p class="label-volume">10ML I 0.3 OZ</p>
      </div>
    </article>
    <article class="label label--marjoram">
      <div class="label-band">VELNIRA BOTANIC</div>
      <div class="label-body">
        <p class="label-claim">100% PURE &amp; NATURAL</p>
        <h2 class="label-title">ESSENTIAL OIL</h2>
        <p class="oil-name">Mayaron</p>
        <p class="oil-latin">Origanum Majorana</p>
        <p class="label-volume">10ML I 0.3 OZ</p>
      </div>
    </article>
  </section>
</main>
</body>
</html>
```